Talvero

I'd like new business card design options. I'll need to provide updated contact info although after the deign is complete. We are in IT, specifically in the data backup, archiving and disaster recovery verticals.

Business

```html
<!DOCTYPE html>
<html lang="en">
<head>
<meta charset="utf-8">
<title>Talvero Business Card</title>
<link rel="stylesheet" href="https://fonts.googleapis.com/css2?family=Roboto:wght@300;400;700&display=swap">
<style>
  :root {
    --page-bg: #e9eaec;
    --card-top: #ffffff;
    --card-bottom: #eceef0;
    --brand-blue: #1f6fbf;
    --deep-blue: #155aa8;
    --light-blue: #3aa6dc;
    --name-blue: #2a82d0;
    --text-grey: #6f7378;
    --rule-blue: #5a9ad6;
  }
  * { margin: 0; padding: 0; box-sizing: border-box; }
  html, body {
    width: 1200px; height: 1023px; overflow: hidden;
    background: var(--page-bg);
    font-family: "Roboto", sans-serif;
  }
  .card {
    position: absolute; left: 150px; top: 254px;
    width: 900px; height: 514px;
    border-radius: 18px; overflow: hidden;
    background: linear-gradient(160deg, var(--card-top) 0%, var(--card-bottom) 100%);
    box-shadow: 0 14px 40px rgba(0,0,0,0.18);
  }
  .brand { position: absolute; left: 62px; top: 78px; }
  .brand-row { display: flex; align-items: center; gap: 16px; }
  .brand-dot { width: 58px; height: 58px; border-radius: 50%; background: var(--light-blue); }
  .brand-name {
    font-weight: 700; font-size: 46px; letter-spacing: 6px;
    color: var(--brand-blue); text-transform: uppercase;
  }
  .brand-tagline {
    margin: 4px 0 0 74px; font-weight: 700; font-size: 17px;
    letter-spacing: 2px; color: var(--light-blue);
  }
  .person { position: absolute; right: 62px; top: 96px; text-align: right; }
  .person-name { font-size: 32px; font-weight: 400; color: var(--name-blue); }
  .person-title {
    margin-top: 6px; padding-bottom: 8px; font-size: 19px; font-weight: 300;
    color: var(--text-grey); border-bottom: 1px solid var(--rule-blue);
  }
  .divider {
    position: absolute; left: 92px; right: 62px; top: 240px;
    height: 1px; background: var(--rule-blue);
  }
  .contacts { position: absolute; left: 96px; top: 272px; list-style: none; }
  .contacts li {
    display: flex; align-items: center; gap: 14px;
    font-size: 21px; font-weight: 300; color: var(--text-grey); line-height: 30px;
  }
  .contacts svg { width: 14px; height: 14px; fill: var(--name-blue); }
  .address {
    position: absolute; right: 62px; top: 268px; text-align: right;
    font-size: 21px; font-weight: 300; color: var(--text-grey); line-height: 30px;
  }
  .footer-stripe {
    position: absolute; left: 0; right: 0; bottom: 40px;
    height: 5px; background: var(--light-blue);
  }
  .footer-band {
    position: absolute; left: 0; right: 0; bottom: 0;
    height: 30px; background: var(--deep-blue);
  }
</style>
</head>
<body>
  <div class="card">
    <div class="brand">
      <div class="brand-row">
        <span class="brand-dot"></span>
        <span class="brand-name">Talvero</span>
      </div>
      <div class="brand-tagline">Backup &amp; Recovery Experts</div>
    </div>

    <div class="person">
      <div class="person-name">Daniel R. Whitford, Ph.D.</div>
      <div class="person-title">President, CTO</div>
    </div>

    <div class="divider"></div>

    <ul class="contacts">
      <li><svg viewBox="0 0 16 16"><path d="M3 1l3 0 1 4-2 1c1 2 3 4 5 5l1-2 4 1 0 3c0 1-1 2-2 2C7 15 1 9 1 3c0-1 1-2 2-2z"/></svg>800.555.0142</li>
      <li><svg viewBox="0 0 16 16"><rect x="1" y="6" width="14" height="8" rx="1"/><rect x="4" y="1" width="8" height="4"/></svg>928.555.0187</li>
      <li><svg viewBox="0 0 16 16"><circle cx="8" cy="8" r="7"/></svg>www.talvero.com</li>
      <li><svg viewBox="0 0 16 16"><path d="M1 3h14v10H1z M2 4l6 5 6-5" fill="none" stroke="#2a82d0" stroke-width="1.6"/></svg>daniel.whitford@talvero.com</li>
    </ul>

    <div class="address">
      240 North Alder Street<br>
      Brookfield, Texas 75210
    </div>

    <div class="footer-stripe"></div>
    <div class="footer-band"></div>
  </div>
</body>
</html>
```